Homepage Design :) --- A website that connects Journalists to Sources to make brilliant news stories

I need a new homepage designed for a company based in California. The homepage is simple.
The website is QuillBridgeConnect.com.

About us:
We are a platform that connects reporters to expert sources (normal people with specific expertise) so a reporter can quickly and easily source information for their news story. Also, the source gets cited in their major news article so it's a win-win situation.

Design:
We have no real slogan except maybe the slogan on the website (beautiful stories that connect us), though that can change too.

I would like to see designs of any style that you choose. We really only have one website color shown in blue on the website, you can use other colors in addition to that one or even change the theme color.

Attachments:
- Homepage to redesign, which you can go to the website yourself to check it out
- A mockup sketch of a revision idea that I had in mind with two people thinking short thoughts. Though this is just a random thought.... You can make anything you want! :)
- An image of what the logged in dashboard looks like just if you want a reference

The footer menu links will remain but can be anything color/style.

Make any ideas you want, keep the same amount of sections or add more, add any graphics or things that you want, etc. I want creativity to really attract customers the second they land on the page. A powerfully beautiful home page!

For reference, some competing websites are NewsDeskLink.com, Vornip.io, and plivex.com
I noticed all these website use red/orange related colors, so maybe I should change the color theme to that? Again, your decision :)

```html
<!DOCTYPE html>
<html lang="en">
<head>
<meta charset="utf-8">
<title>QuillBridge Connect — Homepage</title>
<link rel="stylesheet" href="https://fonts.googleapis.com/css2?family=Archivo:wght@400;500;600;700&display=swap">
<style>
  :root {
    --orange: #f7941d;
    --ink: #111111;
    --ink-soft: #1c1c1c;
    --footer-ink: #1d2a52;
    --paper: #ffffff;
    --backdrop: #ffffff;
    --shadow: rgba(0, 0, 0, 0.18);
  }
  * { box-sizing: border-box; margin: 0; padding: 0; }
  html, body {
    width: 1200px; height: 900px; overflow: hidden;
    background: var(--backdrop);
    font-family: "Archivo", Arial, sans-serif;
    color: var(--ink);
  }
  .page {
    position: absolute; left: 203px; top: 35px;
    width: 846px; height: 833px;
    background: var(--paper);
    box-shadow: 0 0 4px var(--shadow);
  }
  .brand { position: absolute; left: 17px; top: 18px; text-align: center; }
  .brand-name { font-size: 18px; font-weight: 600; letter-spacing: 0.3px; line-height: 22px; }
  .brand-tagline { font-size: 5.5px; font-weight: 600; line-height: 8px; }
  .nav-button {
    position: absolute; top: 12px; width: 78px; height: 36px;
    border: 2.5px solid var(--orange); border-radius: 18px;
    display: flex; align-items: center; justify-content: center;
    font-size: 11.5px; font-weight: 600; color: var(--ink);
    text-decoration: none;
  }
  .nav-signup { left: 659px; }
  .nav-login { left: 750px; }
  .hero-title {
    position: absolute; left: 0; top: 127px; width: 846px;
    text-align: center; color: var(--orange);
    font-size: 52.5px; font-weight: 700; line-height: 62px; letter-spacing: -0.3px;
  }
  .hero-lead {
    position: absolute; left: 0; top: 232px; width: 846px;
    text-align: center; font-size: 17.5px; font-weight: 600; line-height: 24px;
    letter-spacing: -0.2px;
  }
  .divider {
    position: absolute; left: 17px; top: 380px; width: 812px; height: 1px;
    background: var(--orange);
  }
  .section-title {
    position: absolute; left: 0; top: 436px; width: 846px;
    text-align: center; font-size: 41px; font-weight: 600; line-height: 50px;
  }
  .section-intro {
    position: absolute; left: 163px; top: 501px; width: 520px;
    text-align: center; font-size: 17px; font-weight: 400; line-height: 27px;
    color: var(--ink-soft);
  }
  .step {
    position: absolute; top: 604px; width: 231px; height: 131px;
    border: 7.5px solid var(--orange); border-radius: 66px;
    text-align: center;
  }
  .step-1 { left: 17px; }
  .step-2 { left: 309px; }
  .step-3 { left: 599px; }
  .step-title { margin-top: 9px; font-size: 18px; font-weight: 600; line-height: 24px; }
  .step-text {
    width: 176px; margin: 6px auto 0;
    font-size: 9.8px; line-height: 15.7px; color: var(--ink-soft);
  }
  .site-footer {
    position: absolute; left: 0; top: 762px; width: 846px; height: 71px;
    background: var(--orange);
  }
  .footer-col { position: absolute; top: 10px; font-size: 10px; line-height: 14px; color: var(--footer-ink); }
  .footer-col h3 { font-size: 10px; font-weight: 700; color: var(--ink); margin-bottom: 0; }
  .footer-col a { display: block; color: var(--footer-ink); text-decoration: none; }
  .footer-about { left: 17px; }
  .footer-info { left: 156px; }
  .footer-rules { left: 310px; }
</style>
</head>
<body>
  <main class="page">
    <header>
      <div class="brand">
        <div class="brand-name">QBC</div>
        <div class="brand-tagline">QuillBridge Connect Service</div>
      </div>
      <a class="nav-button nav-signup" href="#">Sign Up</a>
      <a class="nav-button nav-login" href="#">Login</a>
    </header>

    <section class="hero">
      <h1 class="hero-title">Beautiful stories that connect us</h1>
      <p class="hero-lead">Find sources for the stories that you need information.<br>Browse profiles of your sources to verify expertise.<br>Explore pitches to discover new topics.</p>
    </section>

    <div class="divider"></div>

    <section class="how-it-works">
      <h2 class="section-title">How it works</h2>
      <p class="section-intro">QuillBridge Connect (QBC) connects reporters and sources from around the world. You want the real, honest stories. We connect you to the experts.</p>

      <div class="step step-1">
        <h3 class="step-title">Step 1</h3>
        <p class="step-text">QuillBridge Connect (QBC) connects reporters and sources from around the world. You want the real, honest stories. We connect you to the experts.</p>
      </div>
      <div class="step step-2">
        <h3 class="step-title">Step 2</h3>
        <p class="step-text">QuillBridge Connect (QBC) connects reporters and sources from around the world. You want the real, honest stories. We connect you to the experts.</p>
      </div>
      <div class="step step-3">
        <h3 class="step-title">Step 3</h3>
        <p class="step-text">QuillBridge Connect (QBC) connects reporters and sources from around the world. You want the real, honest stories. We connect you to the experts.</p>
      </div>
    </section>

    <footer class="site-footer">
      <nav class="footer-col footer-about">
        <h3>About</h3>
        <a href="#">Contact us</a>
        <a href="#">How it works</a>
        <a href="#">Job Board</a>
      </nav>
      <nav class="footer-col footer-info">
        <h3>Information</h3>
        <a href="#">Terms of Service</a>
        <a href="#">Privacy Policy</a>
      </nav>
      <nav class="footer-col footer-rules">
        <h3>Rules</h3>
        <a href="#">Reporter &amp; Source Rules</a>
        <a href="#">Refund Policy</a>
      </nav>
    </footer>
  </main>
</body>
</html>
```